Brand New Africa Focused Specialty Insurance business needs a slick website

Meridian Cover Partners needs a slick website design to launch our business with. we have 3 lines of business to begin with - Political Risk and Trade Credit and Property. (this will extend to 9: Political violence and Terrorism, Construction, Liability, Energy, Aviation, Marine, Parametric and Crisis Management at a later date). We are based in London but are Africa focused and our mission statement Meridian Cover Partners provides comprehensive, bespoke insurance risk mitigating solutions to local and global customers, giving them the confidence to grow their businesses sustainably. our tagline is "protecting Africa". Our colours are purple (Red 36, Green 11, Blue 96) and gold (Red 143, Green 137, Blue 53).

Target Market(s)

Brokers
Businesses across africa

Coding

Number of Pages Required

4 page

Font styles to use
Sans Serif
Other font styles liked:
• Cairo (but open to others too)

Requirements
Must have
• Pages:
1. Home page/about us (to include Lines of Business)
2. a page for Property line (we will need to add a link so that people can send an email to the mailbox)
3. a page for Political Risk and Trade Credit ( we will need to add a link so that people can send an email to the mailbox)
3. a page about our people (photos not yet taken for this)
4. a careers page
we have a lot of text for the above, we just need to fine tune it

must be tied to the colour scheme I detailed above.

the font for the logo is called Cairo
Nice to have
• https://www.tolvane-mu.com/ - we like the look of this website, but perhaps less colour
Should not have
• Any African animal like Lions or Zebras

```html
<!DOCTYPE html>
<html lang="en">
<head>
<meta charset="utf-8">
<title>Meridian Cover Partners — Protecting Africa</title>
<link href="https://fonts.googleapis.com/css2?family=Roboto:wght@400;500;700&family=Saira+Semi+Condensed:wght@600;700&display=swap" rel="stylesheet">
<style>
:root{
  --purple:#240b60;
  --gold:#8f8935;
  --gold-light:#aea86a;
  --ink:#222;
  --muted:#666;
  --soft:#f1f1f1;
  --footer:#f4f4f4;
  --white:#fff;
}
*{box-sizing:border-box;margin:0;padding:0}
html,body{width:1200px;height:4215px;overflow:hidden}
body{font-family:'Roboto',sans-serif;color:var(--ink);background:var(--white);position:relative}
.abs{position:absolute}
section,header,footer{position:absolute;left:0;width:1200px}
h1,h2{font-family:'Saira Semi Condensed',sans-serif;color:var(--purple);font-weight:700;letter-spacing:.3px}
p{line-height:1.6}
.btn{position:absolute;display:flex;align-items:center;justify-content:center;gap:8px;border-radius:30px;color:#fff;font-weight:700;font-size:15px;text-transform:uppercase;background:var(--gold)}
.btn svg{width:15px;height:15px}
.btn.purple{background:var(--purple)}

/* header */
.topline{top:0;height:5px;background:var(--purple)}
.site-header{top:5px;height:100px;z-index:2}
.brand{position:absolute;left:111px;top:24px;display:flex;align-items:center;gap:10px}
.brand-mark{width:58px;height:58px;border:3px solid var(--gold);border-radius:50%}
.brand-name{font-weight:700;font-size:16px;color:var(--purple)}
.nav{position:absolute;top:41px;left:0;font-size:15px;font-weight:500;color:var(--purple)}
.nav span{position:absolute;white-space:nowrap}
.nav .active{color:var(--gold)}
.nav .active::after{content:"";position:absolute;left:0;right:0;top:24px;height:3px;background:var(--gold)}
.lang{display:flex;align-items:center;gap:5px}
.flag{width:14px;height:14px;border-radius:50%;background:linear-gradient(#c8102e 0 0) center/100% 3px no-repeat,linear-gradient(#c8102e 0 0) center/3px 100% no-repeat,#1f3f8f}
.login{position:absolute;left:990px;top:36px;width:96px;height:34px;border-radius:20px;background:var(--gold);color:#fff;font-weight:700;font-size:14px;display:flex;align-items:center;justify-content:center;gap:6px}

/* hero */
.hero{top:0;height:672px;background:linear-gradient(100deg,#e9e9ea 0%,#f2f2f2 45%,#f6f6f6 100%)}
.hero-photo{position:absolute;inset:0;background:radial-gradient(ellipse at 15% 55%,rgba(170,160,150,.35),transparent 45%),radial-gradient(ellipse at 75% 40%,rgba(190,190,195,.3),transparent 50%)}
.hero h1{position:absolute;left:110px;top:230px;font-size:44px}
.hero p{position:absolute;left:112px;top:298px;width:440px;font-size:16.5px;color:#444;line-height:1.75}
.hero .btn{left:113px;top:417px;width:191px;height:50px}
.hero-diagram{position:absolute;left:600px;top:120px}
.diagram-label{position:absolute;font-weight:700;font-size:17px;color:var(--purple);line-height:1.45}

/* benefits */
.benefits{top:672px;height:196px;background:var(--purple);color:#fff}
.benefit{position:absolute;top:0;width:300px}
.benefit .icon{position:absolute;top:23px;left:1px;width:66px;height:66px;border-radius:50%;background:var(--gold);display:flex;align-items:center;justify-content:center}
.benefit .icon svg{width:36px;height:36px}
.benefit h3{position:absolute;top:104px;font-size:17px;font-weight:700}
.benefit p{position:absolute;top:130px;font-size:14px;line-height:1.45;width:290px}
.divider-v{position:absolute;top:12px;width:2px;height:168px;background:#fff}

/* who we are */
.who{top:868px;height:564px}
.photo{position:absolute}
.who .photo{left:111px;top:109px;width:421px;height:346px;border:4px solid #fff;box-shadow:0 2px 10px rgba(0,0,0,.2);background:linear-gradient(160deg,#d9dde2,#a9b0b8 55%,#7b7f86)}
.who h2{position:absolute;left:601px;top:120px;font-size:34px}
.copy{position:absolute;left:600px;width:490px;font-size:14.5px;color:#555;line-height:1.72}
.who .btn{left:601px;top:394px;width:172px;height:46px}

/* services */
.services{top:1432px;height:549px;background:var(--soft)}
.services h2{position:absolute;width:1200px;text-align:center;top:32px;font-size:34px}
.card-img{position:absolute;top:100px;width:308px;height:205px}
.service-card{position:absolute;top:275px;width:283px;height:197px;background:#fff;box-shadow:0 2px 6px rgba(0,0,0,.12);text-align:center}
.service-card .badge{position:absolute;left:107px;top:-32px;width:68px;height:68px;border-radius:50%;background:#fff;display:flex;align-items:center;justify-content:center}
.service-card .badge svg{width:36px;height:36px}
.service-card h3{position:absolute;top:38px;width:100%;font-size:16px;color:var(--purple);font-weight:700}
.service-card p{position:absolute;top:67px;left:14px;right:14px;font-size:14px;color:#777;line-height:1.65}
.more{position:absolute;font-size:14px;font-weight:700;color:var(--gold);display:flex;align-items:center;gap:6px}
.more svg{width:13px;height:13px}
.service-card .more{top:158px;width:100%;justify-content:center}

/* members */
.members{top:1981px;height:551px}
.members .map{position:absolute;left:345px;top:98px;width:185px;height:362px;border-radius:18px;background:linear-gradient(160deg,#b7b27c,#a09a5c)}
.year-badge{position:absolute;left:193px;top:290px;width:75px;height:26px;background:var(--purple);color:#fff;font-size:15px;font-weight:700;display:flex;align-items:center;justify-content:center}
.members .slide-title{position:absolute;left:120px;width:222px;text-align:center;top:325px;font-size:16px;font-weight:500;color:var(--purple)}
.members .slide-text{position:absolute;left:135px;width:192px;text-align:center;top:358px;font-size:12.5px;color:#777;line-height:1.7}
.dots{position:absolute;left:213px;top:421px;display:flex;gap:4px}
.dots i{width:8px;height:8px;border-radius:50%;background:#bbb}
.dots i.on{background:var(--gold)}
.members h2{position:absolute;left:599px;top:115px;font-size:34px}
.members .btn{left:601px;top:391px;width:172px;height:44px}

/* stats */
.stats{top:2532px;height:223px;background:var(--gold);color:#fff;text-align:center}
.stat{position:absolute;top:34px;width:220px}
.stat strong{display:block;font-family:'Saira Semi Condensed',sans-serif;font-size:30px;font-weight:700}
.stat span{display:block;font-size:13px;line-height:1.6;margin-top:2px}
.stats .divider-v{top:30px;height:78px;background:rgba(255,255,255,.55);width:1px}
.stats .btn{left:463px;top:151px;width:275px;height:43px;font-size:15px}

/* bespoke */
.bespoke{top:2755px;height:640px}
.bespoke h2{position:absolute;left:111px;top:128px;font-size:35px;line-height:1.2}
.ticks{position:absolute;left:111px;top:231px;list-style:none;font-size:14.5px;color:#555}
.ticks li{display:flex;align-items:center;gap:15px;height:29.2px}
.ticks svg{width:14px;height:14px;flex:none}
.bespoke .btn{left:110px;top:496px;width:172px;height:43px}
.bespoke .photo{left:642px;top:124px;width:445px;height:423px;background:linear-gradient(140deg,#d8d4cf,#9c8a7b 55%,#5a5d70)}

/* news */
.news{top:3395px;height:457px}
.news h2{position:absolute;width:1200px;text-align:center;top:14px;font-size:34px}
.news-card{position:absolute;top:92px;width:308px;height:249px;background:#fff;box-shadow:0 1px 8px rgba(0,0,0,.12)}
.tag{position:absolute;left:30px;top:21px;width:98px;height:30px;background:var(--purple);color:#fff;font-size:14px;font-weight:700;display:flex;align-items:center;justify-content:center}
.news-card h3{position:absolute;left:30px;top:67px;width:255px;font-size:15.5px;font-weight:500;line-height:1.38;color:#222}
.meta{position:absolute;left:30px;top:117px;font-size:13.5px;color:#666;display:flex;align-items:center;gap:5px}
.meta svg{width:12px;height:12px}
.news-card p{position:absolute;left:30px;top:148px;width:250px;font-size:14px;color:#777;line-height:1.55}
.news-card .more{left:30px;top:212px}

/* footer */
.site-footer{top:3852px;height:299px;background:var(--footer)}
.site-footer .brand{top:78px;left:111px}
.site-footer .brand-mark{width:68px;height:68px}
.site-footer .brand-name{font-size:17px}
.foot-about{position:absolute;left:111px;top:160px;width:250px;font-size:13.5px;color:#666;line-height:1.65}
.foot-col{position:absolute;top:64px}
.foot-col h4{font-size:16px;font-weight:700;color:var(--purple);margin-bottom:19px}
.foot-col li{list-style:none;font-size:13.5px;color:#666;height:25.7px}
.contact-item{position:absolute;left:30px;font-size:13.5px;color:#666;line-height:1.55}
.contact-item b{display:block;color:var(--purple);font-size:12px}
.contact-icon{position:absolute;left:0;width:14px;height:14px}
.to-top{position:absolute;left:1107px;top:275px;width:36px;height:36px;border-radius:50%;background:var(--gold);display:flex;align-items:center;justify-content:center;z-index:3}
.copyright{top:4151px;height:64px;background:var(--purple);color:#fff;font-size:15px;display:flex;align-items:center;justify-content:center}
</style>
</head>
<body>

<div class="abs topline" style="left:0;width:1200px"></div>

<section class="hero">
  <div class="hero-photo" role="img" aria-label="Soft-focus photo of a business team meeting in an office"></div>
  <h1>PROTECTING AFRICA</h1>
  <p>Lorem ipsum dolor sit amet, consectetur adipiscing elit, sed do eiusmod tempor incididunt consequat. Duis aute irure dolor in reprehenderit in voluptate</p>
  <a class="btn">Get Started <svg viewBox="0 0 16 16"><circle cx="8" cy="8" r="8" fill="#fff"/><path d="M6 4.5 9.5 8 6 11.5" stroke="#8f8935" stroke-width="2" fill="none"/></svg></a>

  <svg class="hero-diagram" width="560" height="520" viewBox="0 0 560 520">
    <defs>
      <radialGradient id="teamTone" cx="50%" cy="50%" r="50%">
        <stop offset="0" stop-color="#8a8478" stop-opacity=".55"/>
        <stop offset="1" stop-color="#8a8478" stop-opacity="0"/>
      </radialGradient>
    </defs>
    <circle cx="259" cy="281" r="208" fill="none" stroke="#8f8935" stroke-width="5"/>
    <circle cx="262" cy="300" r="130" fill="url(#teamTone)" role="img" aria-label="Photo of a business team working together"/>
    <circle cx="259" cy="85" r="62" fill="#8f8935"/>
    <circle cx="259" cy="85" r="56" fill="#c9b8a8" role="img" aria-label="Photo of rising bar chart with houses"/>
    <circle cx="87" cy="366" r="62" fill="#8f8935"/>
    <circle cx="87" cy="366" r="56" fill="#b9c2cc" role="img" aria-label="Photo of hands working with charts and a calculator"/>
    <circle cx="440" cy="366" r="62" fill="#8f8935"/>
    <circle cx="440" cy="366" r="56" fill="#cfc9c4" role="img" aria-label="Photo of colleagues discussing at a table"/>
  </svg>
  <div class="diagram-label" style="left:945px;top:148px">Risk Modeling &amp; Early<br>Warning Technology</div>
  <div class="diagram-label" style="left:535px;top:559px">Contingency Planning<br>&amp; Linked Financing</div>
  <div class="diagram-label" style="left:1017px;top:569px">Risk Pooling &amp;<br>Index Insurance</div>
</section>

<header class="site-header">
  <div class="brand"><div class="brand-mark"></div><div class="brand-name">Meridian Cover Partners</div></div>
  <nav class="nav">
    <span class="active" style="left:399px">Home</span>
    <span style="left:460px">About Us</span>
    <span style="left:542px">Who We Insure</span>
    <span style="left:665px">Services</span>
    <span style="left:743px">News</span>
    <span style="left:800px">Contact Us</span>
    <span class="lang" style="left:899px"><i class="flag"></i>(EN) <svg width="10" height="6" viewBox="0 0 10 6"><path d="M0 0h10L5 6z" fill="#240b60"/></svg></span>
  </nav>
  <a class="login"><svg width="11" height="13" viewBox="0 0 11 13"><rect x="0" y="5.5" width="11" height="7.5" rx="1" fill="#fff"/><path d="M2.5 5.5V4a3 3 0 0 1 6 0v1.5" stroke="#fff" stroke-width="1.6" fill="none"/></svg>Login</a>
</header>

<section class="benefits">
  <div class="benefit" style="left:121px">
    <div class="icon"><svg viewBox="0 0 36 36" fill="none" stroke="#fff" stroke-width="2"><path d="M18 4 30 9v9c0 7-5 12-12 14C11 30 6 25 6 18V9z"/><path d="m12 18 4 4 8-8"/></svg></div>
    <h3>Industry recognised</h3>
    <p>Lorem ipsum dolor sit amet, consectetur adipiscing elit, sed do</p>
  </div>
  <div class="divider-v" style="left:422px"></div>
  <div class="benefit" style="left:458px">
    <div class="icon"><svg viewBox="0 0 36 36" fill="none" stroke="#fff" stroke-width="2"><circle cx="18" cy="16" r="9"/><path d="M18 11v10M15.5 13.5h4a2 2 0 0 1 0 4h-3a2 2 0 0 0 0 4h4"/><path d="M6 30h24"/></svg></div>
    <h3>Flexible and easy to use</h3>
    <p>Lorem ipsum dolor sit amet, consectetur adipiscing elit, sed do</p>
  </div>
  <div class="divider-v" style="left:760px"></div>
  <div class="benefit" style="left:797px">
    <div class="icon"><svg viewBox="0 0 36 36" fill="none" stroke="#fff" stroke-width="2"><circle cx="20" cy="18" r="11"/><path d="M20 11v7l5 3M3 14h6M3 19h5M4 24h5"/></svg></div>
    <h3>Rapid time to value</h3>
    <p>Lorem ipsum dolor sit amet, consectetur adipiscing elit, sed do</p>
  </div>
</section>

<section class="who">
  <div class="photo" role="img" aria-label="Photo of a presenter leading a boardroom meeting"></div>
  <h2>WHO WE ARE</h2>
  <p class="copy" style="top:177px">Lorem ipsum dolor sit amet, consectetur adipiscing elit, sed do eiusmod tempor incididunt ut labore et dolore magna aliqua. Ut enim ad minim veniam, quis nostrud exercitation ullamco laboris nisi ut aliquip ex ea commodo consequat. Duis aute irure dolor in reprehenderit in voluptate velit esse cillum dolore eu fugiat nulla pariatur.</p>
  <p class="copy" style="top:311px">Sed ut perspiciatis unde omnis iste natus error sit voluptatem accusantium doloremque laudantium, totam rem aperiam,</p>
  <a class="btn">Read More <svg viewBox="0 0 16 16"><circle cx="8" cy="8" r="8" fill="#fff"/><path d="M6 4.5 9.5 8 6 11.5" stroke="#8f8935" stroke-width="2" fill="none"/></svg></a>
</section>

<section class="services">
  <h2>OUR SERVICES</h2>

  <div class="card-img" style="left:111px;background:linear-gradient(135deg,#2c4f78,#c79a55 60%,#2b3f5c)" role="img" aria-label="Photo of letter tiles spelling political risk on a world map"></div>
  <div class="service-card" style="left:123px">
    <div class="badge"><svg viewBox="0 0 36 36" fill="none" stroke="#8f8935" stroke-width="2"><path d="M4 13 18 5l14 8z"/><path d="M7 15v13M13 15v13M23 15v13M29 15v13M4 31h28"/></svg></div>
    <h3>POLITICAL RISK</h3>
    <p>Sed ut perspiciatis unde omnis iste natus error sit voluptatem accusantium doloremque laudantium,</p>
    <a class="more">READ MORE <svg viewBox="0 0 14 14"><circle cx="7" cy="7" r="6" fill="none" stroke="#8f8935" stroke-width="1.6"/><path d="M5.5 4.5 8 7l-2.5 2.5" stroke="#8f8935" stroke-width="1.6" fill="none"/></svg></a>
  </div>

  <div class="card-img" style="left:447px;background:linear-gradient(120deg,#f2f2f2,#dcdcdc 55%,#9fb4c8)" role="img" aria-label="Photo of a woman paying online with a card at a laptop"></div>
  <div class="service-card" style="left:459px">
    <div class="badge"><svg viewBox="0 0 36 36" fill="none" stroke="#8f8935" stroke-width="2"><rect x="5" y="6" width="22" height="15" rx="2"/><path d="M5 11h22M15 27l6-6h6v8l-4 4h-8z"/></svg></div>
    <h3>TRADE CREDIT</h3>
    <p>Sed ut perspiciatis unde omnis iste natus error sit voluptatem accusantium doloremque laudantium,</p>
    <a class="more">READ MORE <svg viewBox="0 0 14 14"><circle cx="7" cy="7" r="6" fill="none" stroke="#8f8935" stroke-width="1.6"/><path d="M5.5 4.5 8 7l-2.5 2.5" stroke="#8f8935" stroke-width="1.6" fill="none"/></svg></a>
  </div>

  <div class="card-img" style="left:781px;background:linear-gradient(180deg,#8fb3d6,#c9d6e0 45%,#a9a9a3)" role="img" aria-label="Photo of a modern apartment building"></div>
  <div class="service-card" style="left:793px">
    <div class="badge"><svg viewBox="0 0 36 36" fill="none" stroke="#8f8935" stroke-width="2"><path d="M4 16 18 6l14 10"/><path d="M8 14v16h20V14M14 30v-8h8v8M12 18h3M21 18h3"/></svg></div>
    <h3>PROPERTY</h3>
    <p>Sed ut perspiciatis unde omnis iste natus error sit voluptatem accusantium doloremque laudantium,</p>
    <a class="more">READ MORE <svg viewBox="0 0 14 14"><circle cx="7" cy="7" r="6" fill="none" stroke="#8f8935" stroke-width="1.6"/><path d="M5.5 4.5 8 7l-2.5 2.5" stroke="#8f8935" stroke-width="1.6" fill="none"/></svg></a>
  </div>
</section>

<section class="members">
  <div class="map" role="img" aria-label="Map of Africa with the member states highlighted"></div>
  <div class="year-badge">2020</div>
  <div class="slide-title">Lorem ipsum dolor</div>
  <div class="slide-text">Sed ut perspiciatis unde omnis iste natus error sit</div>
  <div class="dots"><i></i><i class="on"></i><i></i></div>
  <h2>MEMBER STATES</h2>
  <p class="copy" style="top:174px">Lorem ipsum dolor sit amet, consectetur adipiscing elit, sed do eiusmod tempor incididunt ut labore et dolore magna aliqua. Ut enim ad minim veniam, quis nostrud exercitation ullamco laboris nisi ut aliquip ex ea commodo consequat. Duis aute irure dolor in reprehenderit in voluptate velit esse cillum dolore eu fugiat nulla pariatur.</p>
  <p class="copy" style="top:308px">Sed ut perspiciatis unde omnis iste natus error sit voluptatem accusantium doloremque laudantium, totam rem aperiam,</p>
  <a class="btn">Contact Us <svg viewBox="0 0 16 16"><circle cx="8" cy="8" r="8" fill="#fff"/><path d="M6 4.5 9.5 8 6 11.5" stroke="#8f8935" stroke-width="2" fill="none"/></svg></a>
</section>

<section class="stats">
  <div class="stat" style="left:109px"><strong>285M US$</strong><span>LOREM IPSUM<br>2020</span></div>
  <div class="divider-v" style="left:345px"></div>
  <div class="stat" style="left:361px"><strong>285M US$</strong><span>LOREM IPSUM<br>2020</span></div>
  <div class="divider-v" style="left:599px"></div>
  <div class="stat" style="left:615px"><strong>285M US$</strong><span>LOREM IPSUM<br>2020</span></div>
  <div class="divider-v" style="left:853px"></div>
  <div class="stat" style="left:869px"><strong>285M US$</strong><span>LOREM IPSUM<br>2020</span></div>
  <a class="btn purple">See Financial Highlights <svg viewBox="0 0 16 16"><circle cx="8" cy="8" r="8" fill="#fff"/><path d="M6 4.5 9.5 8 6 11.5" stroke="#240b60" stroke-width="2" fill="none"/></svg></a>
</section>

<section class="bespoke">
  <h2>BESPOKE INSURANCE RISK<br>MITIGATING SOLUTIONS</h2>
  <ul class="ticks">
    <li><svg viewBox="0 0 14 14"><circle cx="7" cy="7" r="7" fill="#8f8935"/><path d="m3.8 7 2.2 2.2 4.2-4.2" stroke="#fff" stroke-width="1.8" fill="none"/></svg>Lorem ipsum dolor sit amet, consectetur adipiscing elit, sed do</li>
    <li><svg viewBox="0 0 14 14"><circle cx="7" cy="7" r="7" fill="#8f8935"/><path d="m3.8 7 2.2 2.2 4.2-4.2" stroke="#fff" stroke-width="1.8" fill="none"/></svg>Eiusmod tempor incididunt ut labore et dolore magna aliqua.</li>
    <li><svg viewBox="0 0 14 14"><circle cx="7" cy="7" r="7" fill="#8f8935"/><path d="m3.8 7 2.2 2.2 4.2-4.2" stroke="#fff" stroke-width="1.8" fill="none"/></svg>Ut enim ad minim veniam, quis nostrud exercitation ullamco laboris</li>
    <li><svg viewBox="0 0 14 14"><circle cx="7" cy="7" r="7" fill="#8f8935"/><path d="m3.8 7 2.2 2.2 4.2-4.2" stroke="#fff" stroke-width="1.8" fill="none"/></svg>Nisi ut aliquip ex ea commodo consequat.</li>
    <li><svg viewBox="0 0 14 14"><circle cx="7" cy="7" r="7" fill="#8f8935"/><path d="m3.8 7 2.2 2.2 4.2-4.2" stroke="#fff" stroke-width="1.8" fill="none"/></svg>Duis aute irure dolor in reprehenderit in voluptate velit esse cillum</li>
    <li><svg viewBox="0 0 14 14"><circle cx="7" cy="7" r="7" fill="#8f8935"/><path d="m3.8 7 2.2 2.2 4.2-4.2" stroke="#fff" stroke-width="1.8" fill="none"/></svg>Dolore eu fugiat nulla pariatur.</li>
    <li><svg viewBox="0 0 14 14"><circle cx="7" cy="7" r="7" fill="#8f8935"/><path d="m3.8 7 2.2 2.2 4.2-4.2" stroke="#fff" stroke-width="1.8" fill="none"/></svg>Sed ut perspiciatis unde omnis iste natus error sit voluptatem</li>
    <li><svg viewBox="0 0 14 14"><circle cx="7" cy="7" r="7" fill="#8f8935"/><path d="m3.8 7 2.2 2.2 4.2-4.2" stroke="#fff" stroke-width="1.8" fill="none"/></svg>Accusantium doloremque laudantium, totam rem aperiam.</li>
  </ul>
  <a class="btn">Read More <svg viewBox="0 0 16 16"><circle cx="8" cy="8" r="8" fill="#fff"/><path d="M6 4.5 9.5 8 6 11.5" stroke="#8f8935" stroke-width="2" fill="none"/></svg></a>
  <div class="photo" role="img" aria-label="Photo of a couple reviewing insurance papers together on a sofa"></div>
</section>

<section class="news">
  <h2>NEWS</h2>
  <article class="news-card" style="left:111px">
    <div class="tag">Press</div>
    <h3>Lorem ipsum dolor sit consectetur adipiscing elit, sed do</h3>
    <div class="meta"><svg viewBox="0 0 12 12"><circle cx="6" cy="3.5" r="3" fill="#240b60"/><path d="M0 12a6 5 0 0 1 12 0z" fill="#240b60"/></svg>By, David &nbsp;|&nbsp; <svg viewBox="0 0 12 12"><rect x="0" y="1.5" width="12" height="10.5" fill="#240b60"/><rect x="1.5" y="4.5" width="9" height="6" fill="#fff"/></svg>Sept 05, 2020</div>
    <p>Sed ut perspiciatis unde omnis iste natus error accusantium</p>
    <a class="more">LEARN MORE <svg viewBox="0 0 14 14"><circle cx="7" cy="7" r="6" fill="none" stroke="#8f8935" stroke-width="1.6"/><path d="M5.5 4.5 8 7l-2.5 2.5" stroke="#8f8935" stroke-width="1.6" fill="none"/></svg></a>
  </article>
  <article class="news-card" style="left:447px">
    <div class="tag">Press</div>
    <h3>Lorem ipsum dolor sit consectetur adipiscing elit, sed do</h3>
    <div class="meta"><svg viewBox="0 0 12 12"><circle cx="6" cy="3.5" r="3" fill="#240b60"/><path d="M0 12a6 5 0 0 1 12 0z" fill="#240b60"/></svg>By, David &nbsp;|&nbsp; <svg viewBox="0 0 12 12"><rect x="0" y="1.5" width="12" height="10.5" fill="#240b60"/><rect x="1.5" y="4.5" width="9" height="6" fill="#fff"/></svg>Septh 05, 2020</div>
    <p>Sed ut perspiciatis unde omnis iste natus error accusantium</p>
    <a class="more">LEARN MORE <svg viewBox="0 0 14 14"><circle cx="7" cy="7" r="6" fill="none" stroke="#8f8935" stroke-width="1.6"/><path d="M5.5 4.5 8 7l-2.5 2.5" stroke="#8f8935" stroke-width="1.6" fill="none"/></svg></a>
  </article>
  <article class="news-card" style="left:781px">
    <div class="tag">Press</div>
    <h3>Lorem ipsum dolor sit consectetur adipiscing elit, sed do</h3>
    <div class="meta"><svg viewBox="0 0 12 12"><circle cx="6" cy="3.5" r="3" fill="#240b60"/><path d="M0 12a6 5 0 0 1 12 0z" fill="#240b60"/></svg>By, David &nbsp;|&nbsp; <svg viewBox="0 0 12 12"><rect x="0" y="1.5" width="12" height="10.5" fill="#240b60"/><rect x="1.5" y="4.5" width="9" height="6" fill="#fff"/></svg>Sept 05, 2020</div>
    <p>Sed ut perspiciatis unde omnis iste natus error accusantium</p>
    <a class="more">LEARN MORE <svg viewBox="0 0 14 14"><circle cx="7" cy="7" r="6" fill="none" stroke="#8f8935" stroke-width="1.6"/><path d="M5.5 4.5 8 7l-2.5 2.5" stroke="#8f8935" stroke-width="1.6" fill="none"/></svg></a>
  </article>
</section>

<footer class="site-footer">
  <div class="brand"><div class="brand-mark"></div><div class="brand-name">Meridian Cover Partners</div></div>
  <p class="foot-about">Sed ut perspiciatis unde omnis iste natus error sit voluptatem accusantium doloremque laudantium,</p>
  <div class="foot-col" style="left:450px"><h4>Quick Links</h4><ul><li>Home</li><li>About</li><li>Services</li><li>Who We Insure</li><li>Login/Logout</li></ul></div>
  <div class="foot-col" style="left:643px"><h4>About Company</h4><ul><li>Terms of Use</li><li>Terms &amp; Condition</li><li>News</li><li>Contact Us</li><li>FAQ</li></ul></div>
  <div class="foot-col" style="left:856px;width:240px">
    <h4>Contact Us</h4>
    <svg class="contact-icon" style="top:46px" viewBox="0 0 14 14"><path d="M3 1 5.5 3.5 4 5.5a8 8 0 0 0 4.5 4.5l2-1.5L13 11l-1.5 2C6 13 1 8 1 2.5z" fill="#240b60"/></svg>
    <div class="contact-item" style="top:44px"><b>Phone</b>+888 888 8888</div>
    <svg class="contact-icon" style="top:99px" viewBox="0 0 14 14"><rect x="0" y="2" width="14" height="10" fill="#240b60"/><path d="m0 2 7 5 7-5" stroke="#fff" stroke-width="1.2" fill="none"/></svg>
    <div class="contact-item" style="top:96px"><b>Email</b>info@meridiancoverpartners.com</div>
    <svg class="contact-icon" style="top:150px" viewBox="0 0 14 14"><path d="M7 0a5 5 0 0 1 5 5c0 4-5 9-5 9S2 9 2 5a5 5 0 0 1 5-5z" fill="#240b60"/><circle cx="7" cy="5" r="2" fill="#fff"/></svg>
    <div class="contact-item" style="top:147px;width:210px"><b>Location</b>Lorem ipsum dolor sit amet, con elit, sed</div>
  </div>
  <a class="to-top"><svg width="14" height="10" viewBox="0 0 14 10"><path d="M1.5 8 7 2.5 12.5 8" stroke="#fff" stroke-width="2.2" fill="none"/></svg></a>
</footer>

<div class="abs copyright" style="left:0;width:1200px">2020 Copyright - Meridian Cover Partners | All Rights Reserved</div>

</body>
</html>
```